New Business Card Design Project

Want a simple but attention grabbing business card. Back Side having mainly our logo and basic info-the front side a typical business card.

Contact Information for Business Card

Hearth & Tile Interiors
218 NW Larkspur Rd. Suite 207
Ankeny, Iowa 50021

phone- 515.482.7093

website is -htidesigns.com

```html
<!DOCTYPE html>
<html lang="en">
<head>
<meta charset="utf-8">
<title>Hearth &amp; Tile Interiors – Business Cards</title>
<link rel="stylesheet" href="https://fonts.googleapis.com/css2?family=Open+Sans:wght@400;600;700&display=swap">
<style>
  :root {
    --bg: #2b2d31;
    --paper: #f4f4f5;
    --ink: #222428;
    --ink-soft: #3a3d44;
    --orange: #e45a24;
    --blue: #2f7fd1;
    --navy-deep: #071630;
    --navy-mid: #26344d;
    --rule: #c9cbd0;
    --white: #ffffff;
  }
  * { box-sizing: border-box; margin: 0; padding: 0; }
  html, body {
    width: 1200px; height: 900px; overflow: hidden;
    background: var(--bg);
    font-family: "Open Sans", Arial, sans-serif;
  }
  .canvas {
    width: 1200px; height: 900px;
    display: flex; flex-direction: column;
    align-items: center; justify-content: center; gap: 20px;
  }
  .card {
    width: 735px; height: 420px;
    position: relative; overflow: hidden;
    box-shadow: 0 10px 30px rgba(0,0,0,.45);
  }

  /* Front */
  .card-front { background: var(--paper); color: var(--ink); }
  .brand {
    position: absolute; top: 78px; right: 70px;
    display: flex; align-items: center; gap: 12px;
  }
  .brand-mark { width: 18px; height: 18px; background: var(--orange); }
  .brand-name {
    font-weight: 700; font-size: 30px; color: var(--orange);
    letter-spacing: .5px;
  }
  .divider {
    position: absolute; left: 230px; right: 60px; top: 218px;
    height: 1px; background: var(--rule);
  }
  .person { position: absolute; left: 60px; top: 196px; }
  .person-name { font-weight: 700; font-size: 24px; color: var(--ink); }
  .person-title { font-size: 17px; color: var(--ink-soft); margin-top: 2px; }
  .contact-list {
    position: absolute; left: 72px; bottom: 46px;
    list-style: none; font-size: 17px; color: var(--ink-soft);
  }
  .contact-list li { display: flex; align-items: center; gap: 12px; line-height: 28px; }
  .contact-list svg { width: 16px; height: 16px; fill: var(--orange); flex: none; }
  .address {
    position: absolute; right: 60px; bottom: 92px;
    text-align: right; font-size: 17px; line-height: 26px; color: var(--ink-soft);
  }
  .address-company { color: var(--orange); }

  /* Back */
  .card-back {
    background: linear-gradient(120deg, var(--navy-deep) 0%, var(--navy-mid) 45%, #3b4760 60%, var(--navy-deep) 100%);
    color: var(--white);
    display: flex; flex-direction: column; align-items: center; justify-content: center;
  }
  .back-brand { display: flex; align-items: center; gap: 14px; }
  .back-brand .brand-mark { width: 22px; height: 22px; background: var(--orange); }
  .back-brand .brand-name { font-size: 40px; color: var(--orange); }
  .website { margin-top: 34px; font-size: 19px; color: var(--white); letter-spacing: .3px; }
</style>
</head>
<body>
<main class="canvas">

  <section class="card card-front" aria-label="Business card front">
    <div class="brand">
      <span class="brand-mark"></span>
      <span class="brand-name">Hearth &amp; Tile Interiors</span>
    </div>
    <div class="divider"></div>
    <div class="person">
      <p class="person-name">Dana Whitfield</p>
      <p class="person-title">President &amp; CEO</p>
    </div>
    <ul class="contact-list">
      <li>
        <svg viewBox="0 0 24 24" aria-hidden="true"><path d="M6.6 10.8a15.1 15.1 0 0 0 6.6 6.6l2.2-2.2c.3-.3.7-.4 1-.2 1.1.4 2.3.6 3.6.6.6 0 1 .4 1 1V20c0 .6-.4 1-1 1A17 17 0 0 1 3 4c0-.6.4-1 1-1h3.5c.6 0 1 .4 1 1 0 1.3.2 2.5.6 3.6.1.3 0 .7-.2 1z"/></svg>
        <span>515.482.7093</span>
      </li>
      <li>
        <svg viewBox="0 0 24 24" aria-hidden="true"><path d="M6 2h12v5H6zM4 8h16a2 2 0 0 1 2 2v7h-4v5H6v-5H2v-7a2 2 0 0 1 2-2zm4 7v5h8v-5z"/></svg>
        <span>515.482.7094</span>
      </li>
      <li>
        <svg viewBox="0 0 24 24" aria-hidden="true"><path d="M2 5h20v14H2zm2 2v.5l8 5 8-5V7l-8 5z"/></svg>
        <span>info@htidesigns.com</span>
      </li>
    </ul>
    <address class="address" style="font-style:normal">
      <span class="address-company">Hearth &amp; Tile Interiors</span><br>
      218 NW Larkspur Rd. Suite 207<br>
      Ankeny, Iowa 50021
    </address>
  </section>

  <section class="card card-back" aria-label="Business card back">
    <div class="back-brand">
      <span class="brand-mark"></span>
      <span class="brand-name">Hearth &amp; Tile Interiors</span>
    </div>
    <p class="website">www.htidesigns.com</p>
  </section>

</main>
</body>
</html>
```